Fresh new and cool frozen burger box! Come be a part of an amazing project!

Crust Fins and Melts restaurant is expanding into the frozen foods market!
please check out our website to understand the vibe of the company
https://brivanta.ca
this is a line of premium Halal meat, we want to stress our top-notch quality.
we like the orange colours so see what you can do with them. (maybe white and orange combo)
you have lots of creative freedom here, feel free to use the burger photo I am attaching or any image off the website.
logo should be nice and visible.
we want this packaging to really stand out and be special.
Come be a part of an amazing project!
Target Market(s)
Muslim Flails, looking of a quality meat burger. mostly already familiar with our brand
Industry/Entity Type
Frozen food
Look and feel

```html
<!DOCTYPE html>
<html lang="en">
<head>
<meta charset="UTF-8">
<title>Emberly Frozen Burger Box – Front Panel</title>
<link rel="stylesheet" href="https://fonts.googleapis.com/css2?family=Anton&family=Open+Sans:wght@400;800&family=Roboto+Condensed:wght@400&display=swap">
<style>
  :root {
    --backdrop: #fde8cc;
    --orange: #ee962a;
    --orange-deep: #e4782a;
    --ink: #1e1e1e;
    --white: #f6f6f4;
    --wood-dark: #3a2a20;
    --wood-mid: #5a4130;
    --bun: #e9b57a;
  }
  * { margin: 0; padding: 0; box-sizing: border-box; }
  html, body { width: 1200px; height: 840px; overflow: hidden; background: var(--backdrop); }
  .canvas { position: relative; width: 1200px; height: 840px; }
  .front-panel {
    position: absolute; left: 60px; top: 40px; width: 1080px; height: 760px;
    background: var(--orange); overflow: hidden;
  }
  .flame-swirl { position: absolute; inset: 0; }
  .hero-photo { position: absolute; inset: 0; }
  .brand {
    position: absolute; left: 56px; top: 90px;
    display: flex; align-items: center; gap: 22px;
  }
  .brand-dot { width: 74px; height: 74px; border-radius: 50%; background: var(--white); }
  .brand-name {
    font-family: "Anton", sans-serif; font-size: 128px; line-height: 1;
    color: var(--white); letter-spacing: 1px;
  }
  .tagline {
    position: absolute; left: 60px; top: 250px;
    font-family: "Open Sans", sans-serif; font-weight: 800; font-size: 40px;
    color: var(--ink); display: flex; align-items: center; gap: 16px;
  }
  .tagline-dot { width: 10px; height: 10px; border-radius: 50%; background: #d6261f; }
  .product-title {
    position: absolute; left: 58px; top: 370px;
    font-family: "Anton", sans-serif; font-size: 92px; line-height: 1.06;
    color: var(--white); letter-spacing: 1px;
  }
  .quality-line {
    position: absolute; left: 62px; top: 584px;
    font-family: "Anton", sans-serif; font-size: 46px; color: var(--ink);
  }
  .zigzag { position: absolute; left: 60px; top: 640px; }
  .net-weight {
    position: absolute; left: 60px; top: 682px;
    background: var(--ink); color: var(--white); border-radius: 30px;
    padding: 10px 26px; font-family: "Roboto Condensed", sans-serif; font-size: 26px;
  }
  .halal-badge {
    position: absolute; left: 440px; top: 612px; width: 112px; height: 112px;
    border-radius: 50%; border: 5px solid var(--ink); background: var(--orange);
  }
  .storage-note {
    position: absolute; right: 36px; top: 640px; text-align: right;
    font-family: "Roboto Condensed", sans-serif; color: var(--white);
    font-size: 19px; line-height: 1.3;
  }
  .storage-note strong { font-family: "Open Sans", sans-serif; font-weight: 800; font-size: 19px; }
</style>
</head>
<body>
<div class="canvas">
  <section class="front-panel">
    <svg class="flame-swirl" width="1080" height="760" viewBox="0 0 1080 760">
      <path fill="var(--orange-deep)" d="M520 60 C 560 180, 450 260, 470 380 C 490 480, 420 560, 330 620 C 260 680, 290 760, 290 760 L 620 760 L 620 0 Z"/>
    </svg>
    <svg class="hero-photo" width="1080" height="760" viewBox="0 0 1080 760" role="img" aria-label="Photo of a sesame bun burger with beef patty, cheese, bacon, tomato and lettuce on a dark wooden board">
      <defs>
        <linearGradient id="woodTone" x1="0" y1="0" x2="1" y2="0">
          <stop offset="0" stop-color="var(--wood-dark)"/>
          <stop offset="1" stop-color="var(--wood-mid)"/>
        </linearGradient>
        <radialGradient id="burgerTone" cx="0.6" cy="0.5" r="0.5">
          <stop offset="0" stop-color="#8a5a34"/>
          <stop offset="0.55" stop-color="var(--bun)" stop-opacity="0.85"/>
          <stop offset="1" stop-color="var(--bun)" stop-opacity="0"/>
        </radialGradient>
      </defs>
      <path fill="url(#woodTone)" d="M690 0 L1080 0 L1080 760 L560 760 C 600 640, 520 520, 580 360 C 630 220, 620 100, 690 0 Z"/>
      <ellipse cx="860" cy="370" rx="230" ry="320" fill="url(#burgerTone)"/>
    </svg>

    <div class="brand">
      <span class="brand-dot"></span>
      <span class="brand-name">EMBERLY</span>
    </div>
    <div class="tagline">
      <span>Crust</span><span class="tagline-dot"></span>
      <span>Fins</span><span class="tagline-dot"></span>
      <span>Melts</span>
    </div>

    <h1 class="product-title">FROZEN BURGER<br>EMBERLY</h1>
    <p class="quality-line">PREMIUM HALAL MEAT</p>
    <svg class="zigzag" width="380" height="26" viewBox="0 0 380 26">
      <polyline fill="none" stroke="var(--white)" stroke-width="3"
        points="0,22 12,6 24,22 36,6 48,22 60,6 72,22 84,6 96,22 108,6 120,22 132,6 144,22 156,6 168,22 180,6 192,22 204,6 216,22 228,6 240,22 252,6 264,22 276,6 288,22 300,6 312,22 324,6 336,22 348,6 360,22 372,6 380,16"/>
    </svg>
    <div class="net-weight">Net Wt 32 oz (2LB) 907g</div>
    <div class="halal-badge"></div>

    <p class="storage-note"><strong>KEEP FROZEN</strong><br>serving suggestion<br>enlarged to show texture</p>
  </section>
</div>
</body>
</html>
```